Business Card for Managing Partner Investment Fund

To create a business card template for an investment fund manager. Business card should be more professional in nature, not too colorful, more upscale, and created using the attached logos and fund name files. I would prefer a black or gray color scheme, but am open to the use of color as well. I would prefer a double sided business card, but open to single sided business card designs as well. The business card should include: name, title, and contact information, as well as logo and company name. I would prefer a more stream-lined, simple business card design.
Updates
Address: 4190 NE 38th Ter. Ocala, FL 34470
Email: talvin47@quorimail.net
Phone: 561-347-9162
Title: managing partner
Name: Dorian Velsky
Fund Name: Ambergate Capital
Logos can be found in files attached to the brief
Target Market(s)
potential investors, other fund managers
Industry/Entity Type
Finance
Contact Information for Business Card
Name on card: Dorian Velsky
Title: Managing Partner
Colors
Designer to choose colors to be used in the design.
Requirements
Must have
- Phone number
- email address
- physical address
- title
- name
- logo
- Fund name
Nice to have
- simple layout
Should not have
- too many colors, busy fonts,

```html
<!DOCTYPE html>
<html lang="en">
<head>
<meta charset="utf-8">
<title>Ambergate Capital — Business Card</title>
<link href="https://fonts.googleapis.com/css2?family=Montserrat:wght@400;700&display=swap" rel="stylesheet">
<style>
  :root {
    --stage: #3a3b3d;
    --navy: #1c3a56;
    --navy-deep: #16304a;
    --citron: #c9c23a;
    --paper: #efefee;
    --ink: #2a2a2a;
    --muted: #9a9a9a;
  }
  * { box-sizing: border-box; margin: 0; padding: 0; }
  html, body { width: 1200px; height: 901px; overflow: hidden; }
  body {
    background: var(--stage);
    font-family: "Montserrat", sans-serif;
    display: flex;
    flex-direction: column;
    align-items: center;
    justify-content: center;
    gap: 48px;
  }
  .card {
    position: relative;
    width: 640px;
    height: 366px;
    box-shadow: 0 10px 24px rgba(0,0,0,.35);
  }
  .card__pattern {
    position: absolute;
    inset: 0;
    background: linear-gradient(135deg, var(--navy) 0%, #4d5a3e 35%, var(--citron) 50%, #4d5a3e 65%, var(--navy) 100%);
  }
  .card__panel {
    position: absolute;
    inset: 30px;
    background: var(--paper);
    display: flex;
    align-items: center;
    padding: 0 34px 0 40px;
    gap: 40px;
  }
  .wordmark {
    display: flex;
    align-items: center;
    gap: 10px;
    font-weight: 700;
    font-size: 22px;
    letter-spacing: 1px;
    text-transform: uppercase;
    line-height: 1.15;
    color: var(--ink);
  }
  .wordmark__mark {
    width: 14px; height: 14px;
    background: currentColor;
    flex: none;
  }
  .contact { font-size: 13px; color: #555; line-height: 1.45; margin-top: 30px; }
  .contact__name { font-weight: 700; font-size: 18px; color: var(--navy); text-transform: uppercase; letter-spacing: .5px; line-height: 1.1; }
  .contact__title { color: var(--muted); font-size: 13px; margin-bottom: 8px; }
  .contact__address { margin-bottom: 10px; }
  .contact__label { font-weight: 700; color: var(--ink); margin-right: 6px; }
  .card--back .card__panel {
    inset: 46px 60px 70px 60px;
    background: var(--navy-deep);
    justify-content: center;
    padding: 0;
  }
  .card--back .wordmark { color: #f2f2f2; font-size: 26px; }
</style>
</head>
<body>
  <section class="card card--front">
    <div class="card__pattern" role="img" aria-label="Shattered navy and citron abstract pattern border"></div>
    <div class="card__panel">
      <div class="wordmark"><span class="wordmark__mark"></span><span>Ambergate<br>Capital</span></div>
      <div class="contact">
        <p class="contact__name">Dorian Velsky</p>
        <p class="contact__title">Managing Partner</p>
        <p class="contact__address">4190 NE 38th Ter.<br>Ocala<br>FL 34470</p>
        <p><span class="contact__label">Phone:</span>561-347-9162</p>
        <p><span class="contact__label">Email:</span>talvin47@quorimail.net</p>
      </div>
    </div>
  </section>
  <section class="card card--back">
    <div class="card__pattern" role="img" aria-label="Shattered navy and citron abstract pattern background"></div>
    <div class="card__panel">
      <div class="wordmark"><span class="wordmark__mark"></span><span>Ambergate<br>Capital</span></div>
    </div>
  </section>
</body>
</html>
```